Webdesign für freiberuflichen Statiker
Zielgruppe
Ich bin seit 2021 freiberuflicher Statiker. Ich arbeite mit anderen Freelancern / Partnern / Firmen zusammen und lasse von ihnen z.B. Pläne zeichnen. Meine aktuelle Website habe ich selbst designed, mit Wordpress. Diese soll nun aber komplett neu gestaltet werden. Meine Domain www.vendrik-statik.de möchte ich möglichst behalten.
Meine Zielgruppe sind Architekturbüros, Bauträger, private und öffentliche Bauherren. Sie sollen vor allem einen visuellen Eindruck von unserer Arbeit bekommen - durch Fotos (und einem Video auf der Startseite) von Baustellen, von unseren 3D-Modellen oder Berechnungsmodellen.
Aufgabenstellung
Es gibt bereits ein neues Logo. Dieses werde ich mit anhängen. Außerdem habe ich eine pdf-Datei vorbereitet ('SBV_Inhalte Website'), die den groben Aufbau der Website vorgibt und der die Texte entnommen werden können. Auf der ersten Seite des Dokuments stehen außerdem 3 Beispiel-Websites, die ich gut finde und an denen Ihr euch orientieren könnt. Die Farbwahl kann sehr schlicht gehalten werden - ähnlich wie bei den 3 Beispiel-Seiten. Ich liefere eigene Bilder mit, für projektunabhängige Inhalte können aber auch andere Bilder verwendet werden.

```html
<!DOCTYPE html>
<html lang="de">
<head>
<meta charset="utf-8">
<title>SBV – Office</title>
<link rel="stylesheet" href="https://fonts.googleapis.com/css2?family=Montserrat:wght@400;500;600;700&display=swap">
<style>
:root{
  --ink:#0d0d0d;
  --muted:#8a8a8a;
  --rule:#8f8f8f;
  --bg:#ffffff;
  --footer:#050505;
  --footer-text:#f2f2f2;
  --photo-sky:#b9c9e6;
  --photo-mid:#7f93b8;
  --photo-dark:#1e2740;
}
*{margin:0;padding:0;box-sizing:border-box}
html,body{width:1200px;height:2217px;overflow:hidden;background:var(--bg)}
body{font-family:'Montserrat',sans-serif;color:var(--ink);position:relative}
.site-header{position:absolute;left:0;top:0;width:1200px;height:95px;border-bottom:2px solid var(--rule)}
.brand{position:absolute;left:46px;top:26px;font-size:34px;font-weight:700;line-height:40px;color:var(--ink)}
.header-divider{position:absolute;left:712px;top:0;width:2px;height:95px;background:var(--rule)}
.main-nav{position:absolute;top:36px;left:747px;font-size:18.5px;font-weight:700;letter-spacing:.2px}
.main-nav a{position:absolute;white-space:nowrap;text-decoration:none;color:var(--muted)}
.main-nav a.active{color:var(--ink)}
.nav-office{left:0}
.nav-projekte{left:134px}
.nav-expertise{left:298px}
.section{position:absolute;left:0;width:1200px;height:691px;border-bottom:2px solid var(--rule)}
.s-who{top:95px}
.s-how{top:786px}
.s-dev{top:1477px;border-bottom:none}
.photo{position:absolute;top:0;height:689px;background:linear-gradient(160deg,var(--photo-sky) 0%,var(--photo-mid) 45%,var(--photo-dark) 100%)}
.photo-right{left:713px;width:487px}
.photo-left{left:0;width:487px}
.copy{position:absolute;top:48px}
.copy-left{left:44px;width:636px}
.copy-right{left:522px;width:622px}
.subheadline{font-size:17.5px;font-weight:500;color:var(--muted);line-height:22px}
.headline{font-size:37px;font-weight:700;line-height:44px;margin-top:2px;letter-spacing:.3px}
.body-text{font-size:18.6px;font-weight:500;line-height:28.1px;margin-top:23px;letter-spacing:.45px}
.site-footer{position:absolute;left:0;top:2168px;width:1200px;height:49px;background:var(--footer);color:var(--footer-text);font-size:13px}
.copyright{position:absolute;left:44px;top:16px}
.footer-nav a{position:absolute;top:15px;color:var(--footer-text);text-decoration:none;font-size:14px}
</style>
</head>
<body>
<header class="site-header">
  <div class="brand">SBV</div>
  <div class="header-divider"></div>
  <nav class="main-nav">
    <a class="nav-office active" href="#">OFFICE</a>
    <a class="nav-projekte" href="#">PROJEKTE</a>
    <a class="nav-expertise" href="#">EXPERTISE</a>
  </nav>
</header>

<section class="section s-who">
  <div class="copy copy-left">
    <p class="subheadline">SUBHEADLINE</p>
    <h2 class="headline">WHO WE ARE</h2>
    <p class="body-text">Wir sind ein junges, aufstrebendes und leistungsstarkes Team aus Ingenieuren und planen Tragwerke des Hoch- und Industriebaus, egal ob Neubauten, Umbauten oder Revitalisierungen – national wie international. Zudem decken wir den Wärmeschutz mit ab, sodass wir Ihnen eine integrale Tragwerksplanung aus einer Hand anbieten können. Unser Team besteht aus dem geschäftsführenden Inhaber Torben Quast, der dieses Unternehmen 2021 gegründet hat, und Freelancern sowie Partnerbüros aus der ganzen Welt, u.a. Deutschland, Osteuropa und Asien. Durch diese Vielfältigkeit verfügen wir als Team über eine weitgestufte Expertise sowie einen großen internationalen Erfahrungsschatz. Da unsere interne Zusammenarbeit nicht lokal im Büro, sondern ausschließlich virtuell stattfindet, waren wir gezwungen, sämtliche Planungsprozesse zu digitalisieren. Dadurch konnten wir die Qualität und Effizienz unserer Arbeit enorm steigern.</p>
  </div>
  <div class="photo photo-right" role="img" aria-label="Foto: zwei Ingenieure mit Schutzhelm blicken auf eine Baustelle mit Gerüst"></div>
</section>

<section class="section s-how">
  <div class="photo photo-left" role="img" aria-label="Foto: zwei Ingenieure mit Schutzhelm blicken auf eine Baustelle mit Gerüst"></div>
  <div class="copy copy-right">
    <p class="subheadline">SUBHEADLINE</p>
    <h2 class="headline">HOW WE WORK</h2>
    <p class="body-text">Unser größter Ansporn ist es, die Wünsche und Ideen der Architekten und Bauherren umzusetzen und unseren Teil zu einem reibungslosen Rohbau zu beizutragen. Unnötig zu erwähnen, dass für uns dabei die Schonung des Budgets eine zentrale Rolle spielt. Das Mittel der Wahl ist für uns die BIM-basierte 3D-Planung – sowohl bei der Erstellung der Ausführungspläne als auch bei unseren statischen Berechnungen. Ausgehend vom 3D-Architekturmodell (oder bei BIM-Projekten das BIM-Modell) können wir ein 3D-Rohbaumodell für die Erstellung der Ausführungspläne sowie ein 3D-Berechnungsmodell in der Statiksoftware entwickeln. Die Vorteile liegen auf der Hand: Zeitersparnis, Kostenoptimierung, höhere Planungssicherheit und vereinfachter Datenaustausch.</p>
  </div>
</section>

<section class="section s-dev">
  <div class="copy copy-left">
    <p class="subheadline">SUBHEADLINE</p>
    <h2 class="headline">DEVELOPMENT</h2>
    <p class="body-text">Unsere Comfort-Zone ist der Hoch- und Industriebau – aber fordern Sie uns gern heraus! Wir lieben Challenges und wollen uns ständig weiterentwickeln. Unser Augenmerk liegt mehr und mehr auf dem Holz- und Holzhybridbau, da wir Holz als Teil der Lösung zur dringend notwendigen CO2-Reduktion des Bausektors sehen. Mit unserem ersten reinen Holzbauprojekt – OK, die Gründung ist aus Stahlbeton – haben wir einen Anfang gemacht: Ein Einfamilienhaus bestehend aus einer Kombination aus Kehlbalken- und Pfettendach, Holztafelwänden und einer aussteifenden Geschossdecke.</p>
  </div>
  <div class="photo photo-right" role="img" aria-label="Foto: zwei Ingenieure mit Schutzhelm blicken auf eine Baustelle mit Gerüst"></div>
</section>

<footer class="site-footer">
  <span class="copyright">© 2024 pixelfalter-media.com</span>
  <nav class="footer-nav">
    <a href="#" style="left:834px">KONTAKT</a>
    <a href="#" style="left:950px">IMPRESSUM</a>
    <a href="#" style="left:1067px">DATENSCHUTZ</a>
  </nav>
</footer>
</body>
</html>
```